Nanna Keyplate, An IT Company Has New Logo, Need Fresh Business Cards

IT company is called Nanna Keyplate and is displayed nicely with the new logo from here on artflock. Would like a fresh business card look that encompasses the idea that we want clients to Cherish Every Gadget. I love the use of circuitry with hearts as endpoints and x's and o's. It needs to have room for my certification logos of which there are 4 and a KMB Alumni log. I am attaching my current card to illustrate how it has always captured attention, but that was in the early stages of business when I was doing more residential work. I am focused on businesses now, so a level of professionalism is necessary. I would also like the card to lend itself well to additional stationary, email signature, ticketing template for my workboard, etc. For the time being, I need the card for an upcoming conference so that work will come later. Color scheme should be that of the new logo. Thank you and I look forward to the designs.

Target Market(s)

Businesses looking for IT services.

Industry/Entity Type

Information Technology

Contact Information for Business Card

Requirements
Must have
• New logo colors and a warm feel. Possibly a tad feminine as I am female, but appealing to males.
Nice to have
• I would like techy, but no too much so. I like friendly and connecting feels. People LOVED my old card and called me because it gave them a warm feeling.

```html
<!DOCTYPE html>
<html lang="en">
<head>
<meta charset="utf-8">
<title>Nanna Keyplate — Business Cards</title>
<link rel="stylesheet" href="https://fonts.googleapis.com/css2?family=Montserrat:wght@400;500;600&display=swap">
<style>
  :root {
    --backdrop: #d9d9d9;
    --card-dark: #3b3b3c;
    --card-light: #f4f4f4;
    --band-light: #ebebeb;
    --pink: #d4a2cf;
    --green: #a5c64a;
    --ink: #4a4a4c;
    --pale: #e6e6e6;
    --icon: #b58fb4;
  }
  * { margin: 0; padding: 0; box-sizing: border-box; }
  html, body { width: 1200px; height: 834px; overflow: hidden; }
  body {
    background: var(--backdrop);
    font-family: "Montserrat", sans-serif;
    position: relative;
  }
  .card {
    position: absolute;
    top: 262px;
    width: 540px;
    height: 309px;
    box-shadow: 0 10px 28px rgba(0,0,0,.25);
    overflow: hidden;
  }
  /* front card */
  .card-front { left: 40px; background: var(--card-dark); }
  .front-brand {
    position: absolute; top: 92px; left: 0; right: 0;
    display: flex; align-items: center; justify-content: center; gap: 12px;
  }
  .brand-mark { width: 14px; height: 14px; background: var(--pink); }
  .front-name { color: var(--pale); font-weight: 400; font-size: 28px; letter-spacing: 1px; }
  .front-tagline {
    position: absolute; top: 196px; left: 0; right: 0;
    text-align: center; color: var(--pink); font-size: 15px; font-weight: 400;
  }
  .front-band {
    position: absolute; top: 232px; left: 0; right: 0; height: 34px;
    background: var(--band-light);
  }
  /* back card */
  .card-back { left: 620px; background: var(--card-light); }
  .back-brand {
    position: absolute; top: 84px; left: 40px;
  }
  .back-name-row { display: flex; align-items: center; gap: 10px; }
  .back-brand .brand-mark { width: 11px; height: 11px; }
  .back-name { color: var(--ink); font-weight: 500; font-size: 22px; }
  .back-tagline {
    margin-top: 4px; padding-left: 21px;
    color: var(--pink); font-size: 8.5px; letter-spacing: 2px; text-transform: uppercase;
  }
  .contact {
    position: absolute; left: 280px; top: 150px;
  }
  .reach { color: var(--pink); font-size: 20px; font-weight: 500; line-height: 1.15; }
  .phone { color: var(--green); font-size: 24px; font-weight: 600; line-height: 1.15; margin-bottom: 10px; }
  .line { display: flex; align-items: center; gap: 8px; color: var(--ink); font-size: 12px; margin-top: 5px; }
  .line svg { width: 13px; height: 13px; flex: none; }
</style>
</head>
<body>
  <section class="card card-front" aria-label="Card front">
    <div class="front-brand">
      <span class="brand-mark"></span>
      <span class="front-name">Nanna Keyplate</span>
    </div>
    <p class="front-tagline">Computer Care &amp; Repair</p>
    <div class="front-band"></div>
  </section>

  <section class="card card-back" aria-label="Card back">
    <div class="back-brand">
      <div class="back-name-row">
        <span class="brand-mark"></span>
        <span class="back-name">Nanna Keyplate</span>
      </div>
      <p class="back-tagline">Cherish Every Gadget</p>
    </div>
    <div class="contact">
      <p class="reach">Reach Us Today</p>
      <p class="phone">321-555-0148</p>
      <p class="line">
        <svg viewBox="0 0 14 14" fill="none" stroke="var(--icon)" stroke-width="1.2"><rect x="1" y="3" width="12" height="8" rx="1"/><path d="M1.5 3.5 7 8l5.5-4.5"/></svg>
        nanna.keyplate@inboxmail.com
      </p>
      <p class="line">
        <svg viewBox="0 0 14 14" fill="none" stroke="var(--icon)" stroke-width="1.2"><circle cx="7" cy="7" r="5.8"/><ellipse cx="7" cy="7" rx="2.5" ry="5.8"/><path d="M1.2 7h11.6"/></svg>
        www.nanna-keyplate.com
      </p>
    </div>
  </section>
</body>
</html>
```